General Dental Office Business Card

I run a private general dental office in southern California, and would like a refresh/redesign of my business card. I focus on quality care rather than volume. The email address on the uploaded current card should be updated to: info@marbleshoredental.example. The current card's logo is a deboss, but I am open to other ideas. The logo can be refreshed, but it is something that's been with me since the beginning of the office, so I wouldn't want a drastic redesign.
Target Market(s)
Adults 18-99, whoever needs dental services
Industry/Entity Type
Healthcare/Dental
Contact Information for Business Card
Name, Address, Phone, email
Colors
Designer to choose colors to be used in the design.
Requirements
Must have
- Logo (Same as original one in the uploaded file), space on back for appointment time/date

```html
<!DOCTYPE html>
<html lang="en">
<head>
<meta charset="utf-8">
<title>Marble Shore Dental – Business Card</title>
<link href="https://fonts.googleapis.com/css2?family=Source+Sans+3:wght@400&family=Questrial&display=swap" rel="stylesheet">
<style>
  :root {
    --sky: #87d5eb;
    --slate: #939598;
    --slate-text: #808285;
    --paper: #ffffff;
    --canvas: #ffffff;
  }
  * { margin: 0; padding: 0; box-sizing: border-box; }
  html, body { width: 1200px; height: 1200px; overflow: hidden; background: var(--canvas); }
  .stage { position: relative; width: 1200px; height: 1200px; }

  .card {
    position: absolute; top: 162px; width: 430px; height: 773px;
    background: var(--paper); overflow: hidden;
    box-shadow: 14px 18px 26px rgba(0,0,0,0.18);
  }
  .card--front { left: 164px; }
  .card--back { left: 641px; }

  /* Front */
  .brand-dot { position: absolute; left: 156px; top: 68px; width: 124px; height: 124px; border-radius: 50%; background: var(--sky); }
  .brand-name {
    position: absolute; left: 0; width: 100%; top: 204px; text-align: center;
    font-family: "Source Sans 3", sans-serif; font-size: 31px; letter-spacing: 1.5px; color: var(--sky);
  }
  .info-band { position: absolute; left: 0; top: 275px; width: 100%; height: 498px; background: var(--sky); }
  .info-band__notch { position: absolute; left: 185px; top: 0; width: 52px; height: 26px; }
  .dentist {
    position: absolute; left: 174px; top: 72px;
    font-family: "Source Sans 3", sans-serif; font-size: 27px; line-height: 32px; letter-spacing: 1px; color: var(--paper);
  }

  .contact { position: absolute; left: 0; width: 100%; height: 22px; font-family: "Questrial", sans-serif; color: var(--paper); }
  .contact__marker { position: absolute; left: 0; top: 4px; width: 33px; height: 15px; background: var(--slate); }
  .contact__icon { position: absolute; left: 30px; top: 0; width: 22px; height: 22px; }
  .contact__text { position: absolute; left: 57px; top: 0; white-space: nowrap; font-size: 19px; line-height: 22px; }
  .contact--address { top: 249px; }
  .contact--address .contact__text { left: 59px; top: -4px; font-size: 22px; line-height: 31px; }
  .contact--phone { top: 371px; }
  .contact--email { top: 409px; }

  /* Back */
  .back-notch { position: absolute; left: 166px; width: 86px; height: 42px; }
  .back-notch--top { top: 0; }
  .back-notch--bottom { bottom: 0; }
  .slot-label {
    position: absolute; left: 0; width: 100%; text-align: center;
    font-family: "Questrial", sans-serif; font-size: 22px; color: var(--slate-text);
  }
  .slot-label--date { top: 137px; }
  .slot-label--time { top: 238px; }
  .back-ring { position: absolute; left: 95px; top: 352px; width: 226px; height: 226px; border-radius: 50%; border: 13px solid var(--slate); }
  .back-name {
    position: absolute; left: 0; width: 100%; top: 600px; text-align: center;
    font-family: "Source Sans 3", sans-serif; font-size: 21px; letter-spacing: 1.5px; color: var(--slate);
  }
  .website {
    position: absolute; left: 0; width: 100%; top: 675px; text-align: center;
    font-family: "Questrial", sans-serif; font-size: 20px; letter-spacing: 2px; color: var(--slate-text);
  }
</style>
</head>
<body>
<main class="stage">
  <section class="card card--front">
    <div class="brand-dot"></div>
    <div class="brand-name">Marble Shore Dental</div>

    <div class="info-band">
      <svg class="info-band__notch" viewBox="0 0 52 26"><polygon points="0,0 52,0 26,26" fill="#ffffff"/></svg>

      <div class="dentist">Daniel R. Park DDS<br>General Dentistry</div>

      <div class="contact contact--address">
        <span class="contact__marker"></span>
        <svg class="contact__icon" viewBox="0 0 22 22"><circle cx="11" cy="11" r="10" fill="#939598" stroke="#ffffff" stroke-width="1.5"/><path d="M6.5 15.5V10L11 6l4.5 4v5.5z" fill="#ffffff"/></svg>
        <div class="contact__text">1280 Harbor Crest Lane<br>Seabright<br>CA 90417</div>
      </div>

      <div class="contact contact--phone">
        <span class="contact__marker"></span>
        <svg class="contact__icon" viewBox="0 0 22 22"><circle cx="11" cy="11" r="10" fill="#939598" stroke="#ffffff" stroke-width="1.5"/><path d="M13.5 5.5l1.5 1.5-1.5 2.5-1-.5c-.6 1.5-1.6 2.8-3 3.8l.5 1-2.2 1.8-1.3-1.2C8.5 14 12 10 13.5 5.5z" fill="#ffffff"/></svg>
        <div class="contact__text">Phone: +1-555-014-2828</div>
      </div>

      <div class="contact contact--email">
        <span class="contact__marker"></span>
        <svg class="contact__icon" viewBox="0 0 22 22"><circle cx="11" cy="11" r="10" fill="#939598" stroke="#ffffff" stroke-width="1.5"/><rect x="5.5" y="7.5" width="11" height="7.5" fill="none" stroke="#ffffff" stroke-width="1.3"/><path d="M5.5 7.5L11 12l5.5-4.5M5.5 15L9.5 11.2M16.5 15l-4-3.8" fill="none" stroke="#ffffff" stroke-width="1.1"/></svg>
        <div class="contact__text">E-mail: info@marbleshoredental.example</div>
      </div>
    </div>
  </section>

  <section class="card card--back">
    <svg class="back-notch back-notch--top" viewBox="0 0 86 42"><polygon points="0,0 86,0 43,42" fill="#939598"/></svg>
    <div class="slot-label slot-label--date">Appointment Date</div>
    <div class="slot-label slot-label--time">Time</div>
    <div class="back-ring"></div>
    <div class="back-name">Marble Shore Dental</div>
    <div class="website">www.marbleshoredental.example</div>
    <svg class="back-notch back-notch--bottom" viewBox="0 0 86 42"><polygon points="43,0 86,42 0,42" fill="#939598"/></svg>
  </section>
</main>
</body>
</html>
```